Dog care service needs business card design

Our company is Paws Harbour. We provide care for dogs while their owners are away, either through home visits or a holiday stay in the homes of carefully selected minders. Our existing website & Chatterbook cover should provide all the colour cues for our business cards - namely blues, blondes and grey. We have an existing logo (provided).

www.pawsharbourcare.example.au
www.facebook.com/pawsharbourcareau

We wish to clearly communicate our three areas of service "dog minding, home visits, dog walking".

We would like to have the files ready for upload to Printlyne (or similar) for immediate printing.

Target Market(s)

Dog owners who love their dogs like family

Industry/Entity Type

Business

Contact Information for Business Card

Paws Harbour
Ph: 0417 358 904

Font styles to use
Sans Serif

Colors
33a6d7
3176b5

Requirements
Must have
• Logo
• Telephone number
• website
• "Dog minding, home visits, dog walking"
Should not have
• any additional illustrations beyond the logo.

```html
<!DOCTYPE html>
<html lang="en">
<head>
<meta charset="utf-8">
<title>Paws Harbour – Business Card</title>
<link rel="stylesheet" href="https://fonts.googleapis.com/css2?family=Open+Sans:wght@400;600;700&display=swap">
<style>
  :root {
    --blue: #3176b5;
    --sky: #33a6d7;
    --slate: #3d4b5a;
    --white: #ffffff;
    --backdrop: #e9eaec;
  }
  * { margin: 0; padding: 0; box-sizing: border-box; }
  html, body {
    width: 1200px; height: 900px; overflow: hidden;
    background: var(--backdrop);
    font-family: "Open Sans", Arial, sans-serif;
  }
  .canvas { position: relative; width: 1200px; height: 900px; }
  .card {
    position: absolute; left: 320px;
    width: 560px; height: 320px;
    overflow: hidden;
    box-shadow: 0 6px 18px rgba(0,0,0,0.18);
  }
  .card--front { top: 110px; background: var(--white); }
  .card--back  { top: 470px; background: var(--blue); }
  .card__shapes { position: absolute; inset: 0; }

  .brand-name {
    font-weight: 600; color: var(--slate);
    line-height: 1.05;
  }
  .front__brand { position: absolute; left: 28px; top: 24px; font-size: 22px; }
  .front__rule {
    position: absolute; left: 190px; right: 24px; top: 92px;
    height: 2px; background: var(--blue);
  }
  .front__title {
    position: absolute; left: 28px; top: 100px;
    font-weight: 700; font-size: 20px; color: var(--blue); letter-spacing: 0.5px;
  }
  .front__phone {
    position: absolute; left: 28px; top: 128px;
    font-size: 12px; color: var(--blue);
  }
  .front__contact {
    position: absolute; left: 28px; top: 196px;
    color: var(--white); font-size: 13px; line-height: 1.65; list-style: none;
  }
  .front__seal {
    position: absolute; right: 18px; bottom: 14px;
    width: 88px; height: 88px; border-radius: 50%;
    background: var(--white); border: 4px solid var(--sky);
    display: flex; align-items: center; justify-content: center; text-align: center;
  }
  .front__seal .brand-name { font-size: 12px; }

  .back__seal {
    position: absolute; left: 190px; top: 38px;
    width: 180px; height: 180px; border-radius: 50%;
    background: var(--white);
    display: flex; align-items: center; justify-content: center; text-align: center;
  }
  .back__seal .brand-name { font-size: 24px; }
  .back__services {
    position: absolute; left: 0; right: 0; top: 244px; text-align: center;
    color: var(--white); font-weight: 600; font-size: 13px; letter-spacing: 1.5px;
  }
  .back__web {
    position: absolute; left: 0; right: 0; top: 270px; text-align: center;
    color: var(--white); font-size: 10px; opacity: 0.85;
  }
</style>
</head>
<body>
<main class="canvas">
  <section class="card card--front" aria-label="Business card front">
    <svg class="card__shapes" width="560" height="320" viewBox="0 0 560 320">
      <polygon points="0,165 560,150 560,320 0,320" fill="var(--blue)"/>
      <polygon points="400,320 560,230 560,320" fill="var(--white)"/>
    </svg>
    <div class="brand-name front__brand">Paws<br>Harbour</div>
    <div class="front__rule"></div>
    <h1 class="front__title">PAWS HARBOUR</h1>
    <p class="front__phone">Ph: 0417 358 904</p>
    <ul class="front__contact">
      <li>Harbour Vale, New South Wales, Australia 2799</li>
      <li>info@pawsharbourcare.example.au</li>
      <li>0417 358 904</li>
    </ul>
    <div class="front__seal"><span class="brand-name">Paws<br>Harbour</span></div>
  </section>

  <section class="card card--back" aria-label="Business card back">
    <div class="back__seal"><span class="brand-name">Paws<br>Harbour</span></div>
    <p class="back__services">DOG MINDING | HOME VISITS | DOG WALKING</p>
    <p class="back__web">www.pawsharbourcare.example.au</p>
  </section>
</main>
</body>
</html>
```